IT Services company requires a services website design with integrated blog

We at Brambleway Code Haulage primarily provide application migration consultancy (e.g. moving applications from Paneview QR to Paneview 5) and application virtualization (e.g. Dunmore Box-K) consultancy.This process is commonly known as 'packaging' but doesnt involve cardboard boxes ;) (however, I am happy to use that visual analogy if you want to use any box graphics) We also provide application compatibility testing, software auditing and application portfolio management.

We are looking for a complete redesign of our current horrible diy attempt at a website at www.brambleway-example.com. We have had created a rebranded logo (attached files and fonts) and a rebranded business card (also attached) We would like the website to match the same/similar colors and styling as these.

I want to redisgn the website so that the main focus of this website is to show our subject matter expertise with a blog and should take up most of the websites real estate and focus on the home screen. Then if the customer wants, they can use our services to help them in their own application migration/deployment projects by browsing our details in links/buttons somewhere

In any of the designs, please do not include my Velharo or Dunmore partnerships.  Thank you

Target Market(s)

Application packagers / engineers looking for technical articles

Application migration project managers

Industry/Entity Type

Real Estate

Requirements
Must have
• This site is primarily a blog site. The blog should have buttons to share each article on social media site. It should be easy for me to create or edit new blog articles (have technical skills but not creative ones). Each article should also allow for comments (do not require approval but should allow for admin removal) but do not add like/vote buttons because i do not expect large enough traffic and could be determental.

There should be a contact page to host contact information and an email box that goes to enquiries@brambleway-example.com

The other pages should include About us and Services (placeholder text to be used as current site text needs overhauling but original text can be used in the design just remember when placing that the text may shorten or increase etc.)

All text has to be easily editable (no over use of text in images where possible)
Nice to have
• An email notification of new comments to articles sent to webadmin@brambleway-example.com

Newsletter subscription
Should not have
• Do not include vote/like buttons or website counters. Initial traffic is not going to be large enough to warrant these features and may reflect badly on the site.

No logon features. Site content and commenting should be open access

No opinion polls

No why choose us section from current website

Do not include partner information in new site (Velharo and Dunmore)

DO NOT JUST REPLICATE EXISTING WEBSITE FEATURES, PLEASE REFER TO THIS BRIEF. THIS SITE NEEDS TO PRIMARILY BE A BLOG

```html
<!DOCTYPE html>
<html lang="en">
<head>
<meta charset="utf-8">
<title>Brambleway Code Haulage</title>
<link rel="stylesheet" href="https://fonts.googleapis.com/css2?family=PT+Sans:wght@400;700&display=swap">
<style>
:root{
  --backdrop:#e4e4e4;
  --page:#f7f7f7;
  --section:#f3f3f3;
  --blog-bg:#f1f1f1;
  --blue:#4a6ddb;
  --blue-text:#3f63d3;
  --orange:#f2640f;
  --dark-btn:#2e2826;
  --ink:#1d1d1d;
  --grey-text:#6c6c6c;
  --footer:#27262b;
  --footer-text:#a8a8ad;
  --circle-1:#175e8c;
  --circle-2:#2b2a9e;
  --circle-3:#3764c0;
}
*{margin:0;padding:0;box-sizing:border-box}
html,body{width:1200px;height:1000px;overflow:hidden}
body{background:var(--backdrop);font-family:"PT Sans",sans-serif;color:var(--ink);position:relative}
.page{position:absolute;left:355px;top:0;width:530px;height:1000px;background:var(--page)}
.abs{position:absolute}
a{text-decoration:none}

/* header */
.brand{left:43px;top:32px;display:flex;align-items:center;gap:7px}
.brand-dot{width:22px;height:22px;border-radius:50%;background:var(--blue)}
.brand-name{font-size:11px;line-height:12px;color:#5a5a5a}
.nav{left:237px;top:0;display:flex}
.nav-item{width:45px;height:78px;margin-right:19px;text-align:center;font-size:8.5px;line-height:10px;color:#222;padding-top:26px}
.nav-item svg{display:block;margin:0 auto 5px}
.nav-item.is-active{background:var(--blue);color:#fff}

/* blog: main focus */
.blog{left:0;top:96px;width:530px;height:420px;background:var(--blog-bg)}
.blog h2{position:absolute;left:55px;top:26px;font-weight:400;font-size:22px;line-height:26px}
.blog .sub{position:absolute;left:55px;top:54px;font-size:10px;color:var(--blue-text)}
.post{position:absolute;top:92px;width:130px;height:300px}
.post-icon{width:80px;height:80px;border-radius:50%;display:flex;align-items:center;justify-content:center}
.post time{display:block;margin-top:18px;font-size:8.5px;line-height:10.5px;font-weight:700;color:var(--blue-text)}
.post h3{font-size:12px;line-height:14.5px;margin-top:5px}
.post p{font-size:8px;line-height:10.5px;color:#333;margin-top:10px}
.post .btn{position:absolute;left:0;top:278px;width:40px;height:16px;background:var(--blue);font-size:8.5px;line-height:16px;font-weight:400}
.post-rule{position:absolute;top:140px;height:200px;border-left:1.5px dotted #444}
.blog-shadow{left:0;top:516px;width:530px;height:10px;background:linear-gradient(#dcdcdc,rgba(247,247,247,0))}

/* hero */
.hero{left:0;top:530px;width:530px;height:160px;background:linear-gradient(90deg,#d9d3cc 0%,#efe6da 55%,#e8d6bd 100%)}
.hero-media{left:0;top:0;width:300px;height:160px;background:linear-gradient(135deg,#2b4a73 0%,#2d8fae 45%,#3ba04a 100%)}
.hero-copy{left:326px;top:32px;color:var(--grey-text);font-size:13px;line-height:16px}
.hero-copy strong{display:block;color:var(--ink);font-size:18px;line-height:24px;margin-top:2px}
.btn{display:block;text-align:center;color:#fff;font-weight:700}
.btn-orange{left:421px;top:118px;width:64px;height:21px;background:var(--orange);font-size:11px;line-height:21px}

/* expertise */
.expertise{left:0;top:690px;width:530px;height:245px;background:var(--section)}
.expertise h2{position:absolute;left:58px;top:36px;font-weight:400;font-size:17.5px;line-height:22px;color:#222}
.expertise h2 b{color:var(--blue-text)}
.expertise p{position:absolute;left:58px;top:116px;width:197px;font-size:7px;line-height:9.5px;color:#333}
.btn-dark{left:55px;top:178px;width:63px;height:20px;background:var(--dark-btn);font-size:10.5px;line-height:20px}
.expertise-media{left:277px;top:50px;width:212px;height:138px;background:linear-gradient(160deg,#f0eeec 0%,#cfcfcf 60%,#f07a2a 100%);border-radius:3px}

/* footer */
.footer{left:0;top:942px;width:530px;height:58px;background:var(--footer);color:var(--footer-text);font-size:7.2px;text-align:center;line-height:58px}
</style>
</head>
<body>
<div class="page">
  <header>
    <div class="abs brand">
      <div class="brand-dot"></div>
      <div class="brand-name">Brambleway<br>Code Haulage</div>
    </div>
    <nav class="abs nav">
      <a class="nav-item is-active">
        <svg width="13" height="12" viewBox="0 0 13 12"><path d="M6.5 0 0 6h2v6h3.5V8h2v4H11V6h2z" fill="#fff"/></svg>Home</a>
      <a class="nav-item">
        <svg width="14" height="13" viewBox="0 0 14 13" fill="none" stroke="#111" stroke-width="1.4"><circle cx="5" cy="4" r="3"/><path d="M0.7 12.5c0-3 2-4.5 4.3-4.5s4.3 1.5 4.3 4.5z"/><path d="M8.5 1.3a3 3 0 0 1 0 5.4M11 8.2c1.4.6 2.3 2 2.3 4.3"/></svg>About<br>Us</a>
      <a class="nav-item">
        <svg width="13" height="13" viewBox="0 0 13 13" fill="none" stroke="#111" stroke-width="1.5"><path d="M6.5 1 12 3.8v5.4L6.5 12 1 9.2V3.8z"/><path d="M1 3.8 6.5 6.6 12 3.8M6.5 6.6V12"/></svg>Services</a>
      <a class="nav-item">
        <svg width="14" height="11" viewBox="0 0 14 11" fill="none" stroke="#111" stroke-width="1.5"><rect x="0.8" y="0.8" width="12.4" height="9.4" rx="1"/><path d="M1 1.2 7 6l6-4.8"/></svg>Contact<br>Us</a>
    </nav>
  </header>

  <section class="abs blog">
    <h2>Blog</h2>
    <div class="sub">check out our latest project</div>

    <article class="post" style="left:55px">
      <div class="post-icon" style="background:var(--circle-1)">
        <svg width="36" height="29" viewBox="0 0 30 24" fill="none" stroke="#fff" stroke-width="2"><path d="M15 4C11 1.5 6 1.5 2 3v18c4-1.5 9-1.5 13 1 4-2.5 9-2.5 13-1V3c-4-1.5-9-1.5-13 1zM15 4v18M6 8h5M6 12h5M6 16h5M19 8h5M19 12h5M19 16h5"/></svg>
      </div>
      <time>Thursday,<br>08 November 2012 13:46</time>
      <h3>How to run local applications within a Box-K 5 sequence</h3>
      <p>Those of us that are used to Box-K before version 5 may...</p>
      <a class="btn">more</a>
    </article>
    <div class="post-rule" style="left:196px"></div>

    <article class="post" style="left:207px">
      <div class="post-icon" style="background:var(--circle-2)">
        <svg width="36" height="29" viewBox="0 0 30 24" fill="none" stroke="#fff" stroke-width="2"><path d="M15 4C11 1.5 6 1.5 2 3v18c4-1.5 9-1.5 13 1 4-2.5 9-2.5 13-1V3c-4-1.5-9-1.5-13 1zM15 4v18M6 8h5M6 12h5M6 16h5M19 8h5M19 12h5M19 16h5"/></svg>
      </div>
      <time>Thursday,<br>31 May 2012 10:25</time>
      <h3>Isolating Driftglass Browser Within Box-K</h3>
      <p>I recently came across an interesting scenario whilst sequencing Driftglass Browser add-ons.</p>
      <a class="btn">more</a>
    </article>
    <div class="post-rule" style="left:348px"></div>

    <article class="post" style="left:359px">
      <div class="post-icon" style="background:var(--circle-3)">
        <svg width="36" height="29" viewBox="0 0 30 24" fill="none" stroke="#fff" stroke-width="2"><path d="M15 4C11 1.5 6 1.5 2 3v18c4-1.5 9-1.5 13 1 4-2.5 9-2.5 13-1V3c-4-1.5-9-1.5-13 1zM15 4v18M6 8h5M6 12h5M6 16h5M19 8h5M19 12h5M19 16h5"/></svg>
      </div>
      <time>Thursday,<br>31 May 2012 10:16</time>
      <h3>What is a<br>Package Accelerator?</h3>
      <p>Box-K 4.6 SP1 introduces a much hyped feature within the sequencer called 'package accelerators'...</p>
      <a class="btn">more</a>
    </article>
  </section>
  <div class="abs blog-shadow"></div>

  <section class="abs hero">
    <div class="abs hero-media" role="img" aria-label="Laptop showing a desktop and tiled start screen, office background"></div>
    <div class="abs hero-copy">We have a wide<br>range of experience<br>in all aspects of<strong>Code Haulage</strong></div>
    <a class="abs btn btn-orange">more</a>
  </section>

  <section class="abs expertise">
    <h2>We have expertise in<br>all of the leading software<br>logistic <b>technologies</b></h2>
    <p>We have a wide range of experience in all aspects of software logistics. We can assist in managing your software from purchase to delivery and beyond for small and large enterprise projects, software vendors and cloud service operators.</p>
    <a class="abs btn btn-dark">more</a>
    <div class="abs expertise-media" role="img" aria-label="Two desktop monitors showing Paneview QR and Paneview 5 with an orange delivery truck in front"></div>
  </section>

  <footer class="abs footer">Copyright | All Right Reserved 2013 | Terms &amp; Conditions</footer>
</div>
</body>
</html>
```